Looking for a modern elegant home improvment website

Looking for a new Design on current website . Please us www.brambleforkbuilders.com PIctures of recent work and stock photos that were attached , Free estimates , Explaining what we do , Similiar to www. brambleforkbuilders.com which is our current webpage . Colors can be different . I have attached our buisness card as well as our postcard we send out to homes . I would like a modern web page that our costumers can feel is professional so they can have a feeling of trust when they hire us . Our address should be on there . Licenesed & Insured should be somewhere on the page . Our Company Logo should be there as well . It would be nice to have a very modern website with great pictures of home interiors and exteriors . a page describing what we do is very important . facebook link to our page is a must as well as a instagram .
Updates

Reason: Looking for a elegant modern 5 page website with proper spelling and professional looking . I extended the deadline and upgraded .

Reason: Looking for more design options .

Target Market(s)

Home owners , Commerical buisness,

Industry/Entity Type

Home Improvement

Number of Pages Required

5+ page

Font styles to use
Serif

Requirements
Must have
• PIctures of recent work and stock photos that were attached , Free estimates , Explaining what we do , Similiar to www. brambleforkbuilders.com which is our current webpage . Colors can be different . I have attached our buisness card as well as our postcard we send out to homes . I would like a modern web page that our costumers can feel is professional so they can have a feeling of trust when they hire us . Our address should be on there . Licenesed & Insured should be somewhere on the page . Our Company Logo should be there as well .
Nice to have
• It would be nice to have a very modern website with great pictures of home interiors and exteriors . a page describing what we do is very important . facebook link to our page is a must as well as a instagram .

```html
<!DOCTYPE html>
<html lang="en">
<head>
<meta charset="utf-8">
<title>Bramble Fork Builders LLC</title>
<link href="https://fonts.googleapis.com/css2?family=Open+Sans:wght@400;600;700;800&family=Playfair+Display:wght@700&display=swap" rel="stylesheet">
<style>
:root{
  --green:#1f6e3b;
  --green-dark:#175a2f;
  --green-deep:#134a27;
  --ink:#333;
  --muted:#6d6d6d;
  --light:#f1f1f1;
  --white:#fff;
  --line:#dcdcdc;
}
*{margin:0;padding:0;box-sizing:border-box}
html,body{width:1200px;height:2832px;overflow:hidden;background:var(--white)}
body{position:relative;font-family:"Open Sans",Arial,sans-serif;color:var(--ink)}
.abs{position:absolute}

/* header */
.site-header{left:0;top:0;width:1200px;height:144px;background:var(--white)}
.brand{left:140px;top:34px;display:flex;align-items:center;gap:14px}
.brand-mark{width:22px;height:22px;background:var(--green)}
.brand-name{font-family:"Playfair Display",Georgia,serif;font-weight:700;color:var(--green);font-size:24px;line-height:1.15;letter-spacing:.5px}
.brand-name small{display:block;font-size:13px;letter-spacing:4px}
.contact-item{top:20px;display:flex;align-items:center;gap:10px;font-size:11px;line-height:1.35;color:var(--muted)}
.contact-item b{display:block;color:var(--ink);font-size:15px;font-weight:600}
.contact-icon{width:34px;height:34px;border:1px solid var(--line);border-radius:50%;display:flex;align-items:center;justify-content:center}
.main-nav{left:650px;top:92px;display:flex;gap:6px}
.main-nav a{font-size:13px;font-weight:600;color:var(--ink);text-decoration:none;padding:8px 14px;text-transform:uppercase}
.main-nav a.active{background:var(--green);color:var(--white)}

/* hero */
.hero{left:0;top:144px;width:1200px;height:540px;overflow:hidden}
.hero-photo{width:100%;height:100%;background:linear-gradient(120deg,#6b4526 0%,#b07a45 35%,#d7b98d 55%,#8b5a31 80%,#5a3a20 100%)}
.hero-title{right:95px;top:250px;color:var(--white);font-weight:800;font-size:56px;line-height:1.1;text-transform:uppercase;text-align:left;text-shadow:0 2px 6px rgba(0,0,0,.35)}
.hero-arrow{top:250px;width:30px;height:50px;background:var(--green);display:flex;align-items:center;justify-content:center}
.hero-dots{left:560px;top:426px;display:flex;gap:8px}
.hero-dots span{width:9px;height:9px;border-radius:50%;background:rgba(255,255,255,.6)}
.hero-dots span.on{background:var(--white)}

/* services */
.services{left:0;top:640px;width:1200px;height:700px;background:var(--light)}
.section-title{font-size:30px;font-weight:800;color:var(--green-deep);text-transform:uppercase}
.title-bar{width:60px;height:4px;background:var(--green);margin-top:8px}
.btn-outline{font-size:12px;font-weight:600;color:var(--ink);border:1px solid #999;padding:8px 16px;text-transform:uppercase}
.btn-solid{font-size:13px;font-weight:700;color:var(--white);background:var(--green-deep);padding:10px 22px;text-transform:uppercase}
.tile{width:222px;height:208px}
.tile-photo{width:100%;height:100%}
.tile-label{left:12px;bottom:14px;display:flex;align-items:center;gap:8px;color:var(--white);font-size:14px;font-weight:700;text-transform:uppercase;text-shadow:0 1px 3px rgba(0,0,0,.6)}
.tile-label::before{content:"";width:10px;height:10px;background:var(--green)}

/* welcome */
.welcome-text{left:132px;top:1444px;width:520px}
.welcome-text p{font-size:14px;line-height:1.75;color:var(--muted);margin-top:22px}
.welcome-photo{left:720px;top:1420px;width:300px;height:280px;background:linear-gradient(150deg,#e9e4dc,#c9b79a 60%,#8f7a5c)}

/* portfolio */
.portfolio{left:0;top:1880px;width:1200px;height:560px;background:var(--light)}
.circle-btn{width:32px;height:32px;border-radius:50%;border:1px solid #aaa;display:flex;align-items:center;justify-content:center;background:var(--white)}
.folio-label{left:12px;bottom:12px;color:var(--white);font-size:13px;font-weight:700;text-transform:uppercase;display:flex;gap:8px;align-items:center;text-shadow:0 1px 3px rgba(0,0,0,.6)}
.folio-label::before{content:"";width:10px;height:10px;background:var(--green)}

/* footer */
.site-footer{left:0;top:2400px;width:1200px;height:380px;background:var(--green)}
.footer-brand{left:140px;top:95px;display:flex;align-items:center;gap:14px}
.footer-brand .brand-mark{background:var(--white)}
.footer-brand .brand-name{color:var(--white)}
.follow{left:190px;top:244px;display:flex;align-items:center;gap:14px;color:var(--white);font-size:13px;font-weight:700;text-transform:uppercase}
.social{width:30px;height:30px;border-radius:50%;background:#2f72c9}
.footer-col{top:70px;color:var(--white)}
.footer-col h4{font-size:13px;font-weight:700;text-transform:uppercase;margin-bottom:18px}
.footer-col li{list-style:none;font-size:13px;line-height:2;opacity:.9}
.contact-row{display:flex;align-items:center;gap:12px;font-size:13px;margin-bottom:22px;line-height:1.4}
.contact-row i{width:26px;height:26px;border-radius:50%;border:1px solid rgba(255,255,255,.7);flex:none}
.copyright{left:0;top:2780px;width:1200px;height:52px;background:var(--green-deep);color:rgba(255,255,255,.8);font-size:11px;display:flex;align-items:center;justify-content:center}
</style>
</head>
<body>

<header class="site-header abs">
  <div class="brand abs">
    <span class="brand-mark"></span>
    <div class="brand-name">Bramble Fork Builders LLC<small>LICENSED &amp; INSURED</small></div>
  </div>

  <div class="contact-item abs" style="left:650px">
    <span class="contact-icon"><svg width="14" height="18" viewBox="0 0 14 18"><path d="M7 0C3 0 0 3 0 7c0 5 7 11 7 11s7-6 7-11c0-4-3-7-7-7zm0 10a3 3 0 110-6 3 3 0 010 6z" fill="#1f6e3b"/></svg></span>
    <div>48 LARKSPUR AVE<br>FERNVALE, NJ 07990</div>
  </div>
  <div class="contact-item abs" style="left:850px">
    <span class="contact-icon"><svg width="16" height="16" viewBox="0 0 24 24"><path d="M6.6 10.8a15.1 15.1 0 006.6 6.6l2.2-2.2c.3-.3.7-.4 1-.2 1.1.4 2.3.6 3.6.6.6 0 1 .4 1 1V20c0 .6-.4 1-1 1A17 17 0 013 4c0-.6.4-1 1-1h3.5c.6 0 1 .4 1 1 0 1.3.2 2.5.6 3.6.1.3 0 .7-.2 1l-2.3 2.2z" fill="#1f6e3b"/></svg></span>
    <div>WORKING<b>555.214.0836</b></div>
  </div>
  <div class="contact-item abs" style="left:1010px">
    <span class="contact-icon"><svg width="16" height="16" viewBox="0 0 24 24"><path d="M6.6 10.8a15.1 15.1 0 006.6 6.6l2.2-2.2c.3-.3.7-.4 1-.2 1.1.4 2.3.6 3.6.6.6 0 1 .4 1 1V20c0 .6-.4 1-1 1A17 17 0 013 4c0-.6.4-1 1-1h3.5c.6 0 1 .4 1 1 0 1.3.2 2.5.6 3.6.1.3 0 .7-.2 1l-2.3 2.2z" fill="#1f6e3b"/></svg></span>
    <div>CELL<b>555.214.0917</b></div>
  </div>

  <nav class="main-nav abs">
    <a class="active">Home</a><a>About Us</a><a>Features</a><a>Services</a><a>Gallery</a><a>Contact Us</a>
  </nav>
</header>

<section class="hero abs">
  <div class="hero-photo" role="img" aria-label="Warm wood kitchen interior with granite island"></div>
  <h1 class="hero-title abs">Licensed &amp;<br>Fully Insured</h1>
  <div class="hero-arrow abs" style="left:0"><svg width="10" height="16"><path d="M8 2L2 8l6 6" stroke="#fff" stroke-width="2.5" fill="none"/></svg></div>
  <div class="hero-arrow abs" style="right:0"><svg width="10" height="16"><path d="M2 2l6 6-6 6" stroke="#fff" stroke-width="2.5" fill="none"/></svg></div>
  <div class="hero-dots abs"><span class="on"></span><span></span><span></span><span></span></div>
</section>

<section class="services abs">
  <svg class="abs" style="left:0;top:-44px" width="1200" height="120" viewBox="0 0 1200 120" preserveAspectRatio="none">
    <path d="M0 44 Q600 120 1200 44 L1200 120 L0 120Z" fill="#f1f1f1"/>
    <path d="M0 52 Q600 128 1200 52" stroke="#1f6e3b" stroke-width="6" fill="none"/>
  </svg>

  <div class="abs" style="left:132px;top:70px">
    <h2 class="section-title">Our Services</h2>
    <div class="title-bar"></div>
  </div>
  <div class="btn-outline abs" style="left:960px;top:100px">Read More</div>

  <div class="tile abs" style="left:132px;top:164px"><div class="tile-photo" role="img" aria-label="Tiled floor room" style="background:linear-gradient(160deg,#8d8a84,#5e564b)"></div><span class="tile-label abs">Tile &amp; Marble</span></div>
  <div class="tile abs" style="left:368px;top:164px"><div class="tile-photo" role="img" aria-label="Painter rolling a wall" style="background:linear-gradient(160deg,#d8d8d6,#8e8e8e)"></div><span class="tile-label abs">Painting</span></div>
  <div class="tile abs" style="left:608px;top:164px"><div class="tile-photo" role="img" aria-label="Modern bathroom" style="background:linear-gradient(160deg,#cfc6bb,#6b5f52)"></div><span class="tile-label abs">Bathrooms</span></div>
  <div class="tile abs" style="left:844px;top:164px"><div class="tile-photo" role="img" aria-label="Wood kitchen" style="background:linear-gradient(160deg,#b78a5c,#5c3b20)"></div><span class="tile-label abs">Kitchens</span></div>

  <div class="tile abs" style="left:132px;top:392px"><div class="tile-photo" role="img" aria-label="House exterior windows and doors" style="background:linear-gradient(160deg,#c8cfd6,#56606a)"></div><span class="tile-label abs">Windows and Doors</span></div>
  <div class="tile abs" style="left:368px;top:392px"><div class="tile-photo" role="img" aria-label="Paver installation" style="background:linear-gradient(160deg,#b09a86,#6e5c4c)"></div><span class="tile-label abs">Pavers</span></div>
  <div class="tile abs" style="left:608px;top:392px"><div class="tile-photo" role="img" aria-label="Finished basement" style="background:linear-gradient(160deg,#e4e1dc,#8c8478)"></div><span class="tile-label abs">Basements</span></div>
  <div class="tile abs" style="left:844px;top:392px"><div class="tile-photo" role="img" aria-label="Sheetrock installation" style="background:linear-gradient(160deg,#ecebe8,#9b9891)"></div><span class="tile-label abs">Sheetrock</span></div>

  <svg class="abs" style="left:0;top:620px" width="1200" height="80" viewBox="0 0 1200 80" preserveAspectRatio="none">
    <path d="M0 0 Q600 80 1200 0 L1200 80 L0 80Z" fill="#fff"/>
  </svg>
</section>

<section class="welcome-text abs">
  <h2 class="section-title">Welcome to Our Site</h2>
  <div class="title-bar"></div>
  <p>Your home is the most important asset you have, so when you're ready to build or remodel, get yourself the best General Contractor in the business!</p>
  <p>We have been building for over 20 years, specializing in residential construction. We are tile &amp; marble specialists. We build bathrooms, kitchens, additions and much more. Give us a try, we do good work and are very passionate about what we do. We are a family owned business that has been in the construction field for over 20 years.</p>
  <div class="btn-solid" style="display:inline-block;margin-top:26px">Read More</div>
</section>
<div class="welcome-photo abs" role="img" aria-label="Builder measuring a wood panel"></div>

<section class="portfolio abs">
  <svg class="abs" style="left:0;top:-40px" width="1200" height="80" viewBox="0 0 1200 80" preserveAspectRatio="none">
    <path d="M0 40 Q600 0 1200 40 L1200 80 L0 80Z" fill="#f1f1f1"/>
  </svg>
  <div class="abs" style="left:132px;top:160px">
    <h2 class="section-title">Portfolio</h2>
    <div class="title-bar"></div>
  </div>
  <div class="circle-btn abs" style="left:976px;top:176px"><svg width="8" height="12"><path d="M6 1L1 6l5 5" stroke="#555" stroke-width="2" fill="none"/></svg></div>
  <div class="circle-btn abs" style="left:1030px;top:176px"><svg width="8" height="12"><path d="M2 1l5 5-5 5" stroke="#555" stroke-width="2" fill="none"/></svg></div>

  <div class="tile abs" style="left:132px;top:252px"><div class="tile-photo" role="img" aria-label="Completed kitchen project" style="background:linear-gradient(160deg,#a97e55,#4e3320)"></div><span class="folio-label abs">Heading 1</span></div>
  <div class="tile abs" style="left:368px;top:252px"><div class="tile-photo" role="img" aria-label="Completed bathroom project" style="background:linear-gradient(160deg,#dcd6ce,#8a7f72)"></div><span class="folio-label abs">Heading 2</span></div>
  <div class="tile abs" style="left:608px;top:252px"><div class="tile-photo" role="img" aria-label="Completed interior project" style="background:linear-gradient(160deg,#5f6670,#23272d)"></div><span class="folio-label abs">Heading 3</span></div>
  <div class="tile abs" style="left:844px;top:252px"><div class="tile-photo" role="img" aria-label="Completed living room project" style="background:linear-gradient(160deg,#c48e55,#6a4222)"></div><span class="folio-label abs">Heading 4</span></div>
</section>

<footer class="site-footer abs">
  <svg class="abs" style="left:0;top:-30px" width="1200" height="60" viewBox="0 0 1200 60" preserveAspectRatio="none">
    <path d="M0 30 Q600 0 1200 30 L1200 60 L0 60Z" fill="#1f6e3b"/>
  </svg>
  <div class="footer-brand abs">
    <span class="brand-mark"></span>
    <div class="brand-name">Bramble Fork Builders LLC</div>
  </div>
  <div class="follow abs">Follow Us <span class="social"></span><span class="social"></span></div>

  <div class="footer-col abs" style="left:620px">
    <h4>Menu</h4>
    <ul><li>Home</li><li>About Us</li><li>Featured</li><li>Services</li><li>Gallery</li><li>Contact Us</li></ul>
  </div>
  <div class="footer-col abs" style="left:840px">
    <h4>Contact Us</h4>
    <div class="contact-row"><i></i><span>48 Larkspur Ave<br>Fernvale, NJ 07990</span></div>
    <div class="contact-row"><i></i><span>555.214.0836</span></div>
    <div class="contact-row"><i></i><span>hello@brambleforkbuilders.com</span></div>
  </div>
</footer>
<div class="copyright abs">Copyright © 2017 All Rights Reserved</div>

</body>
</html>
```